looking for sleek business card to standout from the crowd!

We are a young biotechnology company looking to help you personalize your health through understanding your genetic make up. We need you help in making a clean but sleek business card design using our new logo. The goal? Any time we give our cards out, people say "nice card!" The feel we are going for is "modern-techy". We don't want to come across as an old, giant pharma company, but not trying to be a hipster either.

Target Market(s)

healthcare and biotechnology industry.

Industry/Entity Type

Biotechnology

Contact Information for Business Card

Info to include on the card will be NAME, TITLE, EMAIL, PHONE. The companies website (www.morvalytics.com) should also be on the card some where. Would like the logo, when printed, to be raised.

Requirements
Must have
• The logo we have attached in the color it is in. Fonts for text should lean toward more professional/tech.
Nice to have
• Prefer white/light color background
Should not have
• cartoons, landscape backgrounds images.

```html
<!DOCTYPE html>
<html lang="en">
<head>
<meta charset="UTF-8">
<title>Morvalytics Business Card</title>
<link href="https://fonts.googleapis.com/css2?family=Exo+2:wght@600&family=Open+Sans:wght@400;700&display=swap" rel="stylesheet">
<style>
  :root {
    --page-bg: #e9e9ec;
    --card-black: #0d0d0e;
    --brand-blue: #1b7fd1;
    --brand-green: #8ccf2f;
    --silver: #c9c9cc;
    --divider: #1d5d94;
  }
  * { margin: 0; padding: 0; box-sizing: border-box; }
  html, body {
    width: 1200px;
    height: 900px;
    overflow: hidden;
    background: var(--page-bg);
    font-family: "Open Sans", Arial, sans-serif;
  }
  .sheet {
    position: relative;
    width: 1200px;
    height: 900px;
    display: flex;
    align-items: center;
    justify-content: center;
    gap: 50px;
  }
  .card {
    position: relative;
    width: 525px;
    height: 300px;
    background: var(--card-black);
    border-radius: 3px;
    box-shadow: 0 6px 18px rgba(0,0,0,0.25);
  }
  /* Front */
  .card-front .brand {
    position: absolute;
    left: 40px;
    top: 132px;
    display: flex;
    align-items: center;
    gap: 8px;
  }
  .brand-name {
    font-family: "Open Sans", Arial, sans-serif;
    font-weight: 700;
    font-size: 26px;
    letter-spacing: 0.5px;
    color: var(--brand-blue);
  }
  .brand-dot {
    width: 26px;
    height: 26px;
    border-radius: 50%;
    background: var(--brand-green);
  }
  .divider {
    position: absolute;
    left: 270px;
    top: 40px;
    width: 1px;
    height: 170px;
    background: var(--divider);
  }
  .details {
    position: absolute;
    left: 292px;
    top: 44px;
  }
  .person-name {
    font-family: "Exo 2", "Open Sans", sans-serif;
    font-weight: 600;
    font-size: 19px;
    letter-spacing: 0.5px;
    color: var(--brand-green);
    line-height: 1;
  }
  .person-title {
    font-size: 12px;
    color: var(--brand-blue);
    margin-top: 3px;
  }
  .contacts {
    list-style: none;
    margin-top: 26px;
  }
  .contacts li {
    display: flex;
    align-items: center;
    gap: 8px;
    font-size: 12.5px;
    color: var(--brand-green);
    line-height: 19px;
  }
  .contacts svg {
    width: 9px;
    height: 9px;
    fill: var(--brand-blue);
    flex: none;
  }
  /* Back */
  .card-back {
    display: flex;
    align-items: center;
    justify-content: center;
  }
  .card-back .brand-name {
    font-size: 40px;
    color: var(--silver);
    letter-spacing: 1px;
  }
</style>
</head>
<body>
<main class="sheet">
  <section class="card card-front" aria-label="Card front">
    <div class="brand">
      <span class="brand-name">MORVALYTICS</span>
      <span class="brand-dot"></span>
    </div>
    <div class="divider"></div>
    <div class="details">
      <h1 class="person-name">DANIEL HARTLEY</h1>
      <p class="person-title">Managing Director</p>
      <ul class="contacts">
        <li>
          <svg viewBox="0 0 10 10" aria-hidden="true"><path d="M2 0.5 L3.6 2.6 L2.8 3.6 Q4 6 6.4 7.2 L7.4 6.4 L9.5 8 L8.4 9.5 Q4.5 9.4 1.6 6.4 Q0.4 4 0.5 1.6 Z"/></svg>
          <span>(044)550192837</span>
        </li>
        <li>
          <svg viewBox="0 0 10 10" aria-hidden="true"><path d="M0.5 2 H9.5 V8.5 H0.5 Z M1.2 2.6 L5 5.6 L8.8 2.6" fill="var(--brand-blue)"/><path d="M1.2 2.7 L5 5.6 L8.8 2.7" stroke="#0d0d0e" stroke-width="0.8" fill="none"/></svg>
          <span>hello@morvalytics.com</span>
        </li>
        <li>
          <svg viewBox="0 0 10 10" aria-hidden="true"><circle cx="5" cy="5" r="4.6"/><path d="M0.6 5 H9.4 M5 0.5 Q2.5 5 5 9.5 M5 0.5 Q7.5 5 5 9.5" stroke="#0d0d0e" stroke-width="0.7" fill="none"/></svg>
          <span>www.morvalytics.com</span>
        </li>
      </ul>
    </div>
  </section>

  <section class="card card-back" aria-label="Card back">
    <span class="brand-name">MORVALYTICS</span>
  </section>
</main>
</body>
</html>
```